Professional Learning Organization for Educators needs a Design Thinking Workshop Flyer

We need a flyer for a series of Introductory Design Thinking workshops we're delivering for education leaders.

We have generated our own version of the flyer with a word template, but want it to look even more professional and eye catching. It is attached.

We had an image that we thought might be good, but pulled it out so we don't bias designers' thinking.
Updates

Reason: We are a bit flexible on the deadline since this is a holiday week and people are traveling

Target Market(s)

Very busy education leaders whose curiosity needs to be stimulated enough to enroll in the course

Industry/Entity Type

Education

Font styles to use
Other font styles liked:
• Century Gothic or something closer to that

Requirements
Must have
• Some version of the text that is on the current flyer that I attached.
Nice to have
• I am very flexible and open right now on this design.

```html
<!DOCTYPE html>
<html lang="en">
<head>
<meta charset="utf-8">
<title>Design Thinking Workshops Flyer</title>
<link rel="stylesheet" href="https://fonts.googleapis.com/css2?family=Didact+Gothic&family=Montserrat:ital,wght@0,700;1,400&display=swap">
<style>
  :root {
    --page-bg: #c4dcfb;
    --paper: #ffffff;
    --ink: #1f1f1f;
    --ink-soft: #444444;
    --title: #4a1a16;
    --panel-deep: #0f3a44;
    --panel-mid: #1c5663;
    --panel-light: #2a6e7c;
    --link: #2a2aa8;
    --fee: #4b2a8c;
    --note-top: #f4f4f4;
    --note-bottom: #d9d9d9;
  }
  * { margin: 0; padding: 0; box-sizing: border-box; }
  html, body { width: 1200px; height: 1200px; overflow: hidden; }
  body { background: var(--page-bg); font-family: "Didact Gothic", sans-serif; color: var(--ink); position: relative; }

  .flyer { position: absolute; left: 263px; top: 48px; width: 680px; height: 1044px; background: var(--paper); overflow: hidden; }

  .content { position: absolute; left: 0; top: 0; width: 396px; height: 100%; }
  .title { position: absolute; left: 32px; top: 26px; font-family: "Montserrat", sans-serif; font-weight: 700; font-size: 30px; line-height: 41px; color: var(--title); white-space: nowrap; }
  .subtitle { position: absolute; left: 32px; top: 118px; font-family: "Montserrat", sans-serif; font-weight: 700; font-size: 22px; line-height: 30px; text-decoration: underline; text-underline-offset: 3px; white-space: nowrap; }
  .intro { position: absolute; left: 47px; top: 196px; width: 322px; font-size: 19px; line-height: 24px; }
  .benefits { position: absolute; left: 68px; top: 424px; width: 316px; list-style: none; font-size: 19px; line-height: 24px; }
  .benefits li { position: relative; padding-left: 21px; margin-bottom: 5px; }
  .benefits li svg { position: absolute; left: 1px; top: 7px; width: 14px; height: 12px; }
  .schedule-note { position: absolute; left: 47px; top: 670px; width: 316px; font-size: 19px; line-height: 24px; }

  .sessions { position: absolute; left: 24px; top: 798px; display: flex; gap: 3px; }
  .session { width: 89px; height: 82px; background: linear-gradient(var(--note-top), var(--note-bottom)); border: 1px solid #c8c8c8; box-shadow: 0 3px 4px rgba(0,0,0,0.25); font-size: 13.5px; line-height: 16px; text-align: center; padding-top: 10px; color: #333; }

  .more { position: absolute; left: 22px; top: 900px; font-size: 19px; line-height: 24px; white-space: nowrap; }
  .more a { color: var(--link); text-decoration: underline; }
  .fees { position: absolute; left: 37px; top: 943px; font-size: 19px; line-height: 24px; white-space: nowrap; }
  .fees .free { color: var(--fee); }

  .panel { position: absolute; left: 396px; top: 0; width: 284px; height: 100%; background: linear-gradient(160deg, var(--panel-light), var(--panel-mid) 45%, var(--panel-deep)); }

  .bubble { position: absolute; }
  .bubble svg { position: absolute; left: 0; top: 0; overflow: visible; }
  .bubble p { position: relative; text-align: center; white-space: nowrap; }
  .bubble.lead p { font-size: 20px; line-height: 23px; padding-top: 7px; }
  .bubble.quote p { font-family: "Montserrat", sans-serif; font-style: italic; font-size: 14px; line-height: 19px; color: var(--ink-soft); }

  .contact { position: absolute; left: 19px; top: 846px; width: 246px; height: 168px; }
  .contact svg { position: absolute; left: 0; top: 0; }
  .contact p { position: relative; text-align: center; padding-top: 46px; font-family: "Montserrat", sans-serif; font-weight: 700; font-size: 14.5px; line-height: 20px; white-space: nowrap; }
  .contact .line-link { text-decoration: underline; }
</style>
</head>
<body>
<main class="flyer">
  <section class="content">
    <h1 class="title">DESIGN THINKING<br>WORKSHOPS</h1>
    <h2 class="subtitle">Designing your way to<br>better solutions.</h2>
    <p class="intro">Northgate Public Schools and Summit Ridge BOCES invite you to discover the power of Design Thinking. During our three session course, you will learn and practice mindsets and tools that help you continuously and creatively improve the experiences of the people you serve by:</p>
    <ul class="benefits">
      <li><svg viewBox="0 0 14 12"><path d="M1 6.5 L5 10.5 L13 1" fill="none" stroke="#1f1f1f" stroke-width="2.2"/></svg>Understanding what your teachers, students and community truly need in their learning and work experiences</li>
      <li><svg viewBox="0 0 14 12"><path d="M1 6.5 L5 10.5 L13 1" fill="none" stroke="#1f1f1f" stroke-width="2.2"/></svg>Designing solutions that better meet their needs</li>
      <li><svg viewBox="0 0 14 12"><path d="M1 6.5 L5 10.5 L13 1" fill="none" stroke="#1f1f1f" stroke-width="2.2"/></svg>Seeking authentic feedback and reactions to these solutions prior to their implementation</li>
    </ul>
    <p class="schedule-note">We are offering this three-session course at four different times in spring semester. Please choose the course that works best for your schedule</p>
    <div class="sessions">
      <div class="session">Monday<br>mornings<br>1/23, 1/30<br>and 2/6</div>
      <div class="session">Tuesday<br>afternoons<br>2/7, 2/14<br>and 2/21</div>
      <div class="session">Wednesday<br>afternoons<br>3/8, 3/15<br>and 3/22</div>
      <div class="session">Wednesday<br>evenings<br>2/8, 2/15<br>and 2/22</div>
    </div>
    <p class="more">Go to <a href="#">www.srboces.org</a> to learn more</p>
    <p class="fees">This course is held in Northgate Public<br>Schools. <span class="free">No fee</span> for NPS leaders.<br>$150 fee for leaders outside of NPS.</p>
  </section>

  <aside class="panel" role="img" aria-label="Deep teal geometric triangle pattern background">
    <div class="bubble lead" style="left:28px; top:26px; width:150px; height:82px;">
      <svg width="150" height="82" viewBox="0 0 150 82"><rect x="0" y="0" width="150" height="78" rx="16" fill="#fff"/><path d="M18 74 L14 92 L38 76 Z" fill="#fff"/></svg>
      <p>What our<br>participants<br>say...</p>
    </div>

    <div class="bubble quote" style="left:22px; top:150px; width:242px; height:190px;">
      <svg width="242" height="190" viewBox="0 0 242 190"><rect x="0" y="0" width="242" height="162" rx="38" fill="#fff"/><path d="M138 156 L158 192 L168 154 Z" fill="#fff"/></svg>
      <p style="padding-top:14px;">“This has been an<br>empowering experience<br>that allowed me to try<br>out dramatic changes in<br>my practice that I<br>wouldn’t have imagined<br>before."</p>
    </div>

    <div class="bubble quote" style="left:20px; top:364px; width:250px; height:170px;">
      <svg width="250" height="170" viewBox="0 0 250 170"><ellipse cx="125" cy="72" rx="125" ry="74" fill="#fff"/><path d="M40 118 L34 168 L82 132 Z" fill="#fff"/></svg>
      <p style="padding-top:14px;">“I never realized<br>how often I’ve guessed<br>and assumed what our<br>teachers and students<br>need – now I have a<br>way to stop guessing!”</p>
    </div>

    <div class="bubble quote" style="left:22px; top:560px; width:240px; height:174px;">
      <svg width="240" height="174" viewBox="0 0 240 174"><rect x="0" y="0" width="240" height="146" rx="40" fill="#fff"/><path d="M148 140 L166 176 L176 138 Z" fill="#fff"/></svg>
      <p style="padding-top:16px;">“I finally have tools to<br>generate truly creative<br>ideas that people<br>actually embrace…<br>because they meet their<br>needs”</p>
    </div>

    <div class="contact">
      <svg width="246" height="168" viewBox="0 0 246 168" fill="#fff">
        <circle cx="62" cy="48" r="38"/><circle cx="122" cy="34" r="34"/><circle cx="184" cy="46" r="38"/>
        <circle cx="218" cy="94" r="28"/><circle cx="188" cy="134" r="32"/><circle cx="124" cy="138" r="30"/>
        <circle cx="62" cy="134" r="32"/><circle cx="28" cy="94" r="28"/><rect x="26" y="40" width="194" height="104"/>
      </svg>
      <p>SUMMIT RIDGE BOCES<br><span class="line-link">www.srboces.org</span><br>Questions?<br><span class="line-link">info@srboces.org</span></p>
    </div>
  </aside>
</main>
</body>
</html>
```